Dog Training, Walking, Pet Sitting business
The Morning Pup
Professional
Carla Whitfield
Owner/Certified Trainer
418 Birch Ln.
Marshfield, MA 02917
morningpup456@mailbox.example
www.morningpup.example
Please include my chatterbook page
www.facebook.example/morningpup1
Also under the company name the tagline is
Any Breed, Any Age, Any Issue
Enter to win an Veltro-Tabby lite Wifi-16 GB. You will be entered into the drawing for every new Dog Training, Walking, and Pet Sitting client you refer. Drawing date TBD. Will annouce on Chatterbook morningpup1.
Time and Date for for 1st Session/Walk/Pet Sit _________________

```html
<!DOCTYPE html>
<html lang="en">
<head>
<meta charset="utf-8">
<title>The Morning Pup – Stationery Set</title>
<link href="https://fonts.googleapis.com/css2?family=Open+Sans:wght@400;700&display=swap" rel="stylesheet">
<style>
  :root{
    --bg:#d6d6d6;
    --green-dark:#3d6a27;
    --green:#5b8c39;
    --green-light:#8fb36c;
    --paper:#ffffff;
    --ink:#3a3a3a;
    --muted:#9a9a9a;
    --shade:#c9cfc3;
    --rule:#dddddd;
  }
  *{box-sizing:border-box;margin:0;padding:0}
  html,body{width:1200px;height:228px;overflow:hidden;background:var(--bg)}
  body{font-family:"Open Sans",Arial,sans-serif;color:var(--ink);position:relative}
  .piece{position:absolute;overflow:hidden;box-shadow:0 1px 2px rgba(0,0,0,.25)}
  .paper{background:var(--paper)}
  .green{background:linear-gradient(135deg,var(--green),var(--green-dark))}
  .brand{display:flex;align-items:center;gap:2px;font-weight:700;line-height:1;white-space:nowrap}
  .brand .mark{display:inline-block;background:currentColor}
  .brand.on-green{color:#fff}
  .brand.on-paper{color:var(--green-dark)}
  .tagline{font-size:3px;line-height:1.2;white-space:nowrap}
  .tiny{font-size:3px;line-height:1.35}
  .micro{font-size:2.2px;line-height:1.4;white-space:nowrap}
  .band{position:absolute;left:0;right:0;background:var(--green)}
  .rule{height:1px;background:var(--rule);margin:3px 0}
  .photo{position:absolute;background:linear-gradient(135deg,var(--shade),#a9b59c)}
  .center{display:flex;flex-direction:column;align-items:center;justify-content:center}
</style>
</head>
<body>

<!-- Mobile screen -->
<div class="piece green center phone-screen" style="left:14px;top:88px;width:36px;height:70px;border-radius:3px">
  <div class="brand on-green" style="font-size:3.6px"><span class="mark" style="width:3.6px;height:3.6px"></span>The Morning Pup</div>
</div>

<!-- Business cards -->
<div class="piece green center card card-front" style="left:58px;top:62px;width:42px;height:25px">
  <div class="brand on-green" style="font-size:4px"><span class="mark" style="width:4px;height:4px"></span>The Morning Pup</div>
  <div class="micro" style="color:#e6f0dc;margin-top:1px">Any Breed, Any Age, Any Issue</div>
</div>
<div class="piece paper card card-back" style="left:104px;top:62px;width:42px;height:25px;padding:3px">
  <div class="micro" style="font-weight:700;color:var(--green-dark)">Carla Whitfield</div>
  <div class="micro">Owner/Certified Trainer</div>
  <div class="micro">418 Birch Ln.</div>
  <div class="micro">Marshfield, MA 02917</div>
  <div class="band" style="bottom:0;height:3px"></div>
</div>
<div class="piece paper center card card-front-white" style="left:58px;top:92px;width:42px;height:25px">
  <div class="brand on-paper" style="font-size:4px"><span class="mark" style="width:4px;height:4px"></span>The Morning Pup</div>
  <div class="band" style="bottom:0;height:3px"></div>
</div>
<div class="piece green card card-back-green" style="left:104px;top:92px;width:42px;height:25px;padding:4px 3px;color:#fff">
  <div class="micro" style="font-size:2px">morningpup456@mailbox.example</div>
  <div class="micro" style="font-size:2px">www.morningpup.example</div>
  <div class="micro" style="font-size:2px">www.chatterbook.example/morningpup1</div>
</div>
<div class="piece paper card referral-card" style="left:58px;top:122px;width:42px;height:25px;padding:2px">
  <div class="tiny" style="font-size:2.2px">Enter to win an Veltro-Tabby lite Wifi-16 GB. You will be entered into the drawing for every new Dog Training, Walking, and Pet Sitting client you refer.</div>
</div>
<div class="piece paper card appointment-card" style="left:104px;top:122px;width:42px;height:25px;padding:2px">
  <div class="tiny" style="font-size:2.2px">Drawing date TBD. Will annouce on Chatterbook morningpup1.</div>
  <div class="tiny" style="font-size:2.2px;margin-top:2px">Time and Date for for 1st Session/Walk/Pet Sit __________</div>
  <div class="band" style="bottom:0;height:2px"></div>
</div>

<!-- Letterhead -->
<div class="piece paper letterhead" style="left:160px;top:22px;width:92px;height:124px;padding:6px">
  <div class="brand on-paper" style="font-size:5px"><span class="mark" style="width:5px;height:5px"></span>The Morning Pup</div>
  <div class="tagline" style="color:var(--green);margin-top:1px">Any Breed, Any Age, Any Issue</div>
  <div class="tiny" style="margin-top:10px">Thank you for trusting us with your dog.</div>
  <div class="tiny">We look forward to every walk together.</div>
  <div style="margin-top:4px">
    <div class="rule"></div>
    <div class="rule"></div>
    <div class="rule"></div>
    <div class="rule"></div>
    <div class="rule" style="width:60%"></div>
  </div>
  <div class="tiny" style="margin-top:6px;font-weight:700">Carla Whitfield</div>
  <div class="band center" style="bottom:0;height:9px;color:#fff">
    <div class="micro">418 Birch Ln. · Marshfield, MA 02917 · www.morningpup.example</div>
  </div>
</div>

<!-- Envelopes -->
<div class="piece green center envelope-green" style="left:264px;top:40px;width:96px;height:56px">
  <div class="brand on-green" style="font-size:6px"><span class="mark" style="width:6px;height:6px"></span>The Morning Pup</div>
</div>
<div class="piece paper envelope-white" style="left:264px;top:104px;width:96px;height:50px;padding:5px">
  <div class="brand on-paper" style="font-size:4px"><span class="mark" style="width:4px;height:4px"></span>The Morning Pup</div>
  <div class="tiny" style="margin-top:1px">418 Birch Ln., Marshfield, MA 02917</div>
  <div class="band" style="bottom:0;height:5px"></div>
</div>

<!-- Second sheet -->
<div class="piece paper second-sheet" style="left:372px;top:28px;width:90px;height:116px;padding:6px">
  <div class="brand on-paper" style="font-size:5px"><span class="mark" style="width:5px;height:5px"></span>The Morning Pup</div>
  <div class="green center" style="margin-top:8px;height:34px;color:#fff;padding:3px">
    <div class="micro" style="font-size:2.6px">Enter to win an Veltro-Tabby lite Wifi-16 GB.</div>
  </div>
  <div style="margin-top:6px">
    <div class="rule"></div>
    <div class="rule"></div>
    <div class="rule"></div>
    <div class="rule" style="width:70%"></div>
  </div>
  <div class="band" style="bottom:0;height:6px"></div>
</div>

<!-- DL envelopes and slip -->
<div class="piece green center slip" style="left:482px;top:60px;width:104px;height:26px">
  <div class="brand on-green" style="font-size:5px"><span class="mark" style="width:5px;height:5px"></span>The Morning Pup</div>
</div>
<div class="piece paper dl-envelope" style="left:482px;top:96px;width:104px;height:30px;padding:4px">
  <div class="brand on-paper" style="font-size:4px"><span class="mark" style="width:4px;height:4px"></span>The Morning Pup</div>
  <div class="band" style="bottom:0;height:4px"></div>
</div>
<div class="piece paper dl-envelope" style="left:482px;top:134px;width:104px;height:30px;padding:4px">
  <div class="tiny">www.morningpup.example</div>
  <div class="band" style="left:auto;width:30px;top:0;bottom:0"></div>
</div>

<!-- Disc and sleeve -->
<svg class="disc" style="position:absolute;left:616px;top:52px" width="70" height="70" viewBox="0 0 70 70">
  <circle cx="35" cy="35" r="34" fill="var(--green)"/>
  <circle cx="35" cy="35" r="22" fill="var(--green-dark)"/>
  <circle cx="35" cy="35" r="6" fill="var(--bg)"/>
</svg>
<div class="piece paper center disc-sleeve" style="left:608px;top:130px;width:86px;height:28px">
  <div class="brand on-paper" style="font-size:4.5px"><span class="mark" style="width:4.5px;height:4.5px"></span>The Morning Pup</div>
  <div class="band" style="bottom:0;height:3px"></div>
</div>

<!-- Notepad -->
<div class="piece paper notepad" style="left:708px;top:40px;width:44px;height:100px;padding:4px">
  <div class="brand on-paper" style="font-size:3.5px"><span class="mark" style="width:3.5px;height:3.5px"></span>The Morning Pup</div>
  <div class="band" style="bottom:0;height:8px"></div>
</div>

<!-- Presentation folder -->
<div class="piece paper folder-inside" style="left:766px;top:12px;width:206px;height:196px">
  <div class="band" style="bottom:0;height:40px;background:var(--green-light)"></div>
  <div class="band" style="bottom:0;height:10px"></div>
</div>
<div class="piece paper folder-cover" style="left:976px;top:12px;width:210px;height:196px;padding:12px 14px">
  <div class="brand on-paper" style="font-size:9px"><span class="mark" style="width:9px;height:9px"></span>The Morning Pup</div>
  <div class="tagline" style="font-size:5px;color:var(--green);margin-top:2px">Any Breed, Any Age, Any Issue</div>
  <div class="photo" role="img" aria-label="Silhouettes of several dogs in soft green and grey tones" style="left:110px;right:0;top:60px;bottom:10px"></div>
  <div class="band" style="bottom:0;height:10px"></div>
</div>

</body>
</html>
```